The title of the book is: Resonant Foundations for Builders
I need a front and back cover for my new book.
This is a reference book written to teach architects the basics of acoustics and sound.
The subtitle is: The handbook on echoes and tone most designers hoped their teachers had given them
Author is: Dorian Wick
Publisher: PLOV Press
Primary colors desired are deep red, and deep rich gold. A splash of cobalt blue might be nice too.
Black and/or White fonts
I'm a fan of art deco designs, but I'm also a minimalist, so I'd like something that's not too busy.
This will be used for both a paperback and ebook. Format for "portrait" viewing.
Final files need to be high-res .jpg. Size: 1873 pixels on the longest side, 1600 pixels on the shortest side (350 dpi)
The inside cover page is attached as a reference only.

Target Market(s)

Architects

Industry/Entity Type

Architecture, interior design, and pro audio

Font styles to use
Sans Serif
Other font styles liked:
• Arial

Colors
0054AA
0677BA
7BADD7
CADEEF
E8F1F8
FFC000
F8CF3A
FAE287
FDF2CF
FEFAEE
EB3D1F
EC4F4E
F09395
F8D3D4
FCEDEE

Requirements
Must have
• Elegant font cover design
Nice to have
• Spine and back cover design to compliment front cover. Spine will be roughly 1/2"
Should not have
• Anything that will date the book based on front cover graphics

```html
<!DOCTYPE html>
<html lang="en">
<head>
<meta charset="utf-8">
<title>Resonant Foundations for Builders — Cover Spread</title>
<link rel="stylesheet" href="https://fonts.googleapis.com/css2?family=Arimo:wght@400;700&display=swap">
<style>
  :root {
    --paper: #ffffff;
    --ink: #000000;
    --deep-red: #8b0d11;
    --cobalt-dark: #03285c;
    --cobalt: #0046a8;
    --gold: #d1a514;
    --gold-deep: #b48e10;
    --gold-wave: #e0b30c;
    --type-light: #ffffff;
  }
  html, body {
    margin: 0;
    padding: 0;
    width: 1200px;
    height: 718px;
    overflow: hidden;
    background: var(--paper);
  }
  .spread {
    display: block;
    width: 1200px;
    height: 718px;
    font-family: "Arimo", Arial, sans-serif;
  }
  .panel-label { font-weight: 700; font-size: 52px; fill: var(--ink); }
  .title-strong { font-weight: 700; fill: var(--type-light); }
  .title-light { font-weight: 400; fill: var(--type-light); }
  .frame-line { stroke: var(--gold); stroke-width: 2.5; fill: none; }
  .band-rule { stroke: var(--gold-deep); stroke-width: 5; fill: none; }
  .wave-line { stroke: var(--gold-wave); stroke-width: 11; fill: none; }
  .field-red { fill: var(--deep-red); }
</style>
</head>
<body>
<svg class="spread" viewBox="0 0 2482 1484" preserveAspectRatio="none" xmlns="http://www.w3.org/2000/svg" role="img" aria-label="Book cover spread: back, spine and front of Resonant Foundations for Builders">
  <defs>
    <linearGradient id="cobalt-field" x1="0" y1="640" x2="0" y2="1223" gradientUnits="userSpaceOnUse">
      <stop offset="0" stop-color="var(--cobalt-dark)"/>
      <stop offset="1" stop-color="var(--cobalt)"/>
    </linearGradient>

    <g id="plain-frame">
      <rect class="frame-line" x="40" y="40" width="965" height="1143"/>
    </g>
  </defs>

  <rect x="1.5" y="1.5" width="2479" height="1481" fill="var(--paper)" stroke="var(--ink)" stroke-width="3"/>

  <text class="panel-label" x="615" y="127" text-anchor="middle">BACK</text>
  <text class="panel-label" x="1241" y="127" text-anchor="middle">SPINE</text>
  <text class="panel-label" x="1866" y="127" text-anchor="middle">FRONT</text>

  <!-- Back cover -->
  <svg class="cover-back" x="92" y="170" width="1045" height="1223" viewBox="0 0 1045 1223">
    <rect class="field-red" width="1045" height="1223"/>
    <path fill="url(#cobalt-field)" d="M0,642 C180,780 330,850 508,875 C700,905 900,910 1045,948 V1223 H0 Z"/>
    <path class="wave-line" d="M0,642 C180,780 330,850 508,875 C700,905 900,910 1045,948"/>
    <use href="#plain-frame"/>
    <text class="title-strong" x="515" y="448" text-anchor="middle" font-size="86">RESONANT</text>
    <text class="title-strong" x="515" y="538" text-anchor="middle" font-size="86">FOUNDATIONS</text>
    <text class="title-light" x="515" y="602" text-anchor="middle" font-size="54">FOR BUILDERS</text>
    <text class="title-strong" x="523" y="1053" text-anchor="middle" font-size="26">Publisher: PLOV Press</text>
  </svg>

  <!-- Spine -->
  <svg class="cover-spine" x="1192" y="170" width="98" height="1223" viewBox="0 0 98 1223">
    <rect class="field-red" width="98" height="1223"/>
    <path fill="url(#cobalt-field)" d="M0,960 C40,985 65,1025 98,1045 V1223 H0 Z"/>
    <path class="wave-line" d="M0,960 C40,985 65,1025 98,1045"/>
    <path class="band-rule" d="M0,127 H98 M0,1095 H98"/>
    <text transform="translate(40,275) rotate(90)" font-size="30">
      <tspan class="title-strong">RESONANT FOUNDATIONS</tspan><tspan class="title-light"> FOR BUILDERS</tspan>
    </text>
  </svg>

  <!-- Front cover -->
  <svg class="cover-front" x="1344" y="172" width="1045" height="1223" viewBox="0 0 1045 1223">
    <rect class="field-red" width="1045" height="1223"/>
    <path fill="url(#cobalt-field)" d="M0,1068 C40,1085 150,1095 300,1070 C550,1030 800,900 946,855 C1010,850 1035,875 1045,903 V1223 H0 Z"/>
    <path class="wave-line" d="M0,1068 C40,1085 150,1095 300,1070 C550,1030 800,900 946,855 C1010,850 1035,875 1045,903"/>
    <use href="#plain-frame"/>
    <text class="title-strong" x="928" y="400" text-anchor="end" font-size="108">RESONANT</text>
    <text class="title-strong" x="928" y="500" text-anchor="end" font-size="108">FOUNDATIONS</text>
    <text class="title-light" x="928" y="573" text-anchor="end" font-size="58">FOR BUILDERS</text>
    <text class="title-light" x="928" y="618" text-anchor="end" font-size="21">The handbook on echoes and tone most designers</text>
    <text class="title-light" x="928" y="642" text-anchor="end" font-size="21">hoped their teachers had given them</text>
    <text class="title-light" x="911" y="1033" text-anchor="end" font-size="48">Dorian Wick</text>
  </svg>
</svg>
</body>
</html>
```